Podcast Cover Art for Fast Growing Show (Ill include a gracious tip!)

This artwork is for "The Steadfast Fellow Show." The podcast is for men, and it's all about self-improvement, confidence, success, money, women and masculinity. It's for the guy who wants to improve himself. I'd like for my picture to be included — in black and white — and I want the text to read: "The Steadfast Fellow Show" and somewhere in there it'll say: "with Dale Prowen." I'm open to color schemes. The podcast is a little edgy so I'd like for that to be represented in the design. Thank you! (((Here's the podcast page if you wanna check it out: http://steadfastfellowshow.castorbit.net/)))

Target Market(s)

Men who want to attract women and improve their lives!

Font styles to use
Serif

Colors

Designer to choose colors to be used in the design.

Requirements
Must have
• My image in it (in black and white) and the two titles: "The Steadfast Fellow Show" and "with Dale Prowen"
Nice to have
• My logo in it somehow (which is the arrow looking logo attached below). I've also found that my image looks best in black and white and with a circular type cut out (although I'm open to different design ideas). I've attached my logo with a circular cut out below so you can see what I'm talking about.
Should not have
• Flowers. Teddy bears. ice cream.

```html
<!DOCTYPE html>
<html lang="en">
<head>
<meta charset="utf-8">
<title>The Steadfast Fellow Show – Cover Art</title>
<link rel="stylesheet" href="https://fonts.googleapis.com/css2?family=Anton&family=Montserrat:wght@800&display=swap">
<style>
  :root {
    --concrete-light: #ececec;
    --concrete-dark: #c9c9c9;
    --ink: #0d0d0d;
    --signal-red: #f41a24;
    --photo-light: #8a8a8a;
    --photo-dark: #1c1c1c;
  }
  html, body {
    margin: 0;
    padding: 0;
    overflow: hidden;
    background: #ffffff;
  }
  .cover {
    position: relative;
    width: 1200px;
    height: 1200px;
    overflow: hidden;
    background: radial-gradient(circle at 45% 40%, var(--concrete-light) 0%, #dedede 55%, var(--concrete-dark) 100%);
  }
  .cover__art {
    position: absolute;
    inset: 0;
    width: 1200px;
    height: 1200px;
  }
  .frame-line {
    stroke: var(--ink);
    stroke-width: 11;
    fill: none;
  }
  .host-photo { fill: url(#hostPhotoTone); }
  .title-band { fill: var(--ink); }
  .title-small,
  .title-feature,
  .title-main {
    font-family: "Anton", "Impact", sans-serif;
    text-transform: uppercase;
  }
  .title-small, .title-main { fill: var(--ink); }
  .title-feature { fill: var(--signal-red); }
  .host-credit {
    font-family: "Montserrat", "Arial", sans-serif;
    font-weight: 800;
    fill: var(--ink);
    text-transform: uppercase;
  }
</style>
</head>
<body>
  <main class="cover">
    <svg class="cover__art" viewBox="0 0 1200 1200" xmlns="http://www.w3.org/2000/svg">
      <defs>
        <linearGradient id="hostPhotoTone" x1="0" y1="0" x2="0" y2="1">
          <stop offset="0" stop-color="var(--photo-dark)"/>
          <stop offset="0.35" stop-color="var(--photo-light)"/>
          <stop offset="0.6" stop-color="#3a3a3a"/>
          <stop offset="1" stop-color="var(--photo-dark)"/>
        </linearGradient>
      </defs>

      <g class="frame">
        <line class="frame-line" x1="85" y1="90" x2="1128" y2="90"/>
        <line class="frame-line" x1="90" y1="85" x2="90" y2="1125"/>
        <line class="frame-line" x1="1123" y1="85" x2="1123" y2="1125"/>
        <line class="frame-line" x1="85" y1="1120" x2="302" y2="1120"/>
        <line class="frame-line" x1="916" y1="1120" x2="1128" y2="1120"/>
      </g>

      <path class="host-photo" role="img" aria-label="Black and white portrait of the host, Dale Prowen, hands steepled under his chin, wearing a dark knit sweater"
            d="M500 110 Q510 30 620 28 Q740 30 760 130 L770 390 Q1000 420 1070 640 L230 640 Q300 420 500 395 Z"/>

      <text class="title-small" x="155" y="618" font-size="111" textLength="71" lengthAdjust="spacingAndGlyphs">The</text>

      <g class="title-band-group" transform="rotate(-1.8 606 752)">
        <rect class="title-band" x="62" y="620" width="1090" height="266"/>
        <text class="title-feature" x="121" y="845" font-size="262" textLength="969" lengthAdjust="spacingAndGlyphs">Steadfast</text>
      </g>

      <text class="title-main" x="149" y="1105" font-size="280" textLength="922" lengthAdjust="spacingAndGlyphs">Fellow Show</text>

      <text class="host-credit" x="609" y="1162" font-size="49" text-anchor="middle" textLength="580" lengthAdjust="spacingAndGlyphs">With Dale Prowen</text>
    </svg>
  </main>
</body>
</html>
```